Northgate Signal Shield LLC

Need help designing a web page for an alarm company. I want to promote my business.

Target Market(s)

Residential and commercial clients

Industry/Entity Type

Security Service

Coding

Coded - Design and coding required

Number of Pages Required

2 page

Font styles to use
Sans Serif

Requirements
Must have
• I would llike my logo displayed on the page. I would like my slogan displayed as well
´´A GREAT PLACE FOR YOUR SECURITY NEEDS´´
We are licensed and insured
Company phone number 713-555-0142
Company hours: Monday-Friday 8am-5pm Company address: P.O. Box 419 Crosby, TX 77064 over 25 years experience
Email info. Northgatess@ferntopmail.com
Company license #K52948316
Fire license# TMV-6614027
JLP-8170326
We offer alarm monitoring,security cameras, access control,gate openers, home theater systems, covert camera installations, FIre alarm installation and monitoring
Nice to have
• We offer security at competitive prices.
Get customer information for a free quote similar to brx website.
Should not have
• No prices listed on website

```html
<!DOCTYPE html>
<html lang="en">
<head>
<meta charset="utf-8">
<title>Northgate Signal Shield LLC</title>
<link href="https://fonts.googleapis.com/css2?family=Open+Sans:wght@400;500;600;700;800&display=swap" rel="stylesheet">
<style>
  :root {
    --nav-bg: #30343a;
    --section-dark: #464241;
    --band-red: #a52a2a;
    --white: #ffffff;
    --ink: #2b2b2b;
    --muted: #8a8e93;
    --field-border: #cfd4d9;
    --label-blue: #2b5c9c;
    --label-red: #8c1f1c;
    --label-orange: #b4551b;
    --button: #343a40;
    --logo-green: #2f6b2f;
    --footer-ink: #3a3736;
  }
  * { box-sizing: border-box; margin: 0; padding: 0; }
  html, body { width: 1200px; height: 4488px; overflow: hidden; }
  body { position: relative; background: var(--white); font-family: "Open Sans", Arial, sans-serif; color: var(--ink); }
  .abs { position: absolute; }

  /* navigation */
  .site-nav { left: 0; top: 0; width: 1200px; height: 90px; background: var(--nav-bg); }
  .brand-box { left: 59px; top: 5px; width: 79px; height: 80px; background: var(--white); display: flex; flex-direction: column; align-items: center; justify-content: center; gap: 5px; }
  .brand-dot { width: 18px; height: 18px; border-radius: 50%; background: var(--logo-green); }
  .brand-name { font-size: 11px; font-weight: 700; color: var(--logo-green); }
  .nav-links { left: 185px; top: 34px; display: flex; align-items: baseline; gap: 12px; }
  .nav-links a { text-decoration: none; color: var(--muted); font-size: 12px; }
  .nav-links .nav-main { color: var(--white); font-size: 15px; margin-right: 10px; }
  .nav-links .active { color: var(--white); font-weight: 600; }

  /* hero */
  .hero { left: 0; top: 90px; width: 1200px; height: 675px; background: linear-gradient(120deg, #f1efee 0%, #e6e3e2 45%, #cfc6c2 75%, #b88f84 100%); }
  .hero-title { left: 384px; top: 357px; background: #000; color: var(--white); font-size: 29px; font-weight: 500; line-height: 36px; padding: 0 2px; white-space: nowrap; }
  .hero-sub { left: 395px; top: 428px; background: #000; color: var(--white); font-size: 11px; line-height: 16px; padding: 0 2px; white-space: nowrap; }
  .hero-arrow { top: 417px; width: 14px; height: 20px; }

  /* services */
  .services { left: 0; top: 765px; width: 1200px; height: 1782px; background: var(--section-dark); }
  .band { left: 16px; width: 1168px; height: 73px; background: var(--band-red); color: var(--white); font-size: 30px; font-weight: 500; display: flex; align-items: center; justify-content: center; }
  .service-photo { left: 209px; width: 782px; }

  /* about */
  .about-heading { left: 293px; top: 2547px; font-size: 22px; font-weight: 500; line-height: 32px; white-space: nowrap; }
  .about-text { font-size: 19px; line-height: 28px; color: var(--ink); }
  .about-circle { border-radius: 50%; }

  /* contact */
  .contact-title { left: 107px; top: 3764px; width: 120px; text-align: center; font-size: 20px; line-height: 26px; font-weight: 500; }
  .offer-photo { width: 232px; height: 161px; top: 3771px; }
  .offer-label { top: 3851px; width: 165px; height: 110px; color: var(--white); font-size: 24px; line-height: 30px; text-align: center; display: flex; flex-direction: column; justify-content: center; overflow: hidden; white-space: nowrap; }
  .offer-label b { font-weight: 800; }

  .field-label { font-size: 12px; color: var(--ink); }
  .field { height: 29px; border: 1px solid var(--field-border); border-radius: 4px; background: var(--white); font-size: 12px; color: #6c757d; padding: 6px 10px; line-height: 16px; }
  .select-caret { position: absolute; right: 8px; top: 9px; }
  .check-row { left: 165px; top: 4245px; font-size: 12px; display: flex; align-items: center; gap: 6px; }
  .check-box { width: 11px; height: 11px; border: 1px solid #8a8a8a; border-radius: 2px; }
  .send-button { left: 165px; top: 4270px; width: 100px; height: 29px; background: var(--button); color: var(--white); font-size: 12px; border-radius: 4px; display: flex; align-items: center; justify-content: center; }

  /* footer */
  .site-footer { left: 0; top: 4331px; width: 1200px; height: 157px; background: var(--section-dark); }
  .footer-text { left: 122px; top: 130px; width: 958px; text-align: center; font-size: 9px; color: var(--footer-ink); line-height: 12px; white-space: nowrap; }
</style>
</head>
<body>

<header class="abs site-nav">
  <div class="abs brand-box">
    <span class="brand-dot"></span>
    <span class="brand-name">Northgate</span>
  </div>
  <nav class="abs nav-links">
    <a class="nav-main" href="#">Home</a>
    <a class="active" href="#">Home</a>
    <a href="#">Features</a>
    <a href="#">Pricing</a>
    <a href="#">Blog</a>
  </nav>
</header>

<section class="abs hero" role="img" aria-label="Hand entering a code on a white alarm keypad"></section>
<h1 class="abs hero-title">Most exciting new system</h1>
<p class="abs hero-sub">we are Offering offering 25% off accessories with a starter kit</p>
<svg class="abs hero-arrow" style="left:84px" viewBox="0 0 14 20"><path d="M11 2 L3 10 L11 18" fill="none" stroke="#ffffff" stroke-width="2.5" opacity=".8"/></svg>
<svg class="abs hero-arrow" style="left:1102px" viewBox="0 0 14 20"><path d="M3 2 L11 10 L3 18" fill="none" stroke="#ffffff" stroke-width="2.5" opacity=".8"/></svg>

<section class="abs services">
  <h2 class="abs band" style="top:17px">detect fires quickly and safely</h2>
  <div class="abs service-photo" style="top:108px;height:388px;background:linear-gradient(180deg,#1a0e0d 0%,#4a1210 45%,#8c2a10 75%,#e0651a 100%)" role="img" aria-label="Smoke detector on a ceiling above flames"></div>
  <h2 class="abs band" style="top:514px">Detect Burglars Early</h2>
  <div class="abs service-photo" style="top:604px;height:518px;background:linear-gradient(100deg,#1c1a1c 0%,#7a4a24 35%,#b06a34 60%,#c9b9a3 85%,#8f8a86 100%)" role="img" aria-label="Gloved hand forcing a wooden door with a crowbar"></div>
  <h2 class="abs band" style="top:1141px">Save Your Car</h2>
  <div class="abs service-photo" style="top:1231px;height:518px;background:linear-gradient(135deg,#cfd3d6 0%,#9aa1a8 40%,#3a55a8 65%,#6d7a86 100%)" role="img" aria-label="Hand holding a phone showing a car alarm app in a parking lot"></div>
</section>

<h2 class="abs about-heading">– About Us –</h2>
<p class="abs about-text" style="left:467px;top:2620px;width:412px">“A GREAT PLACE FOR YOUR SECURITY NEEDS.” Northgate Signal Shield LLC is licensed and insured, with over 25 years experience. We offer alarm monitoring, security cameras, access control, gate openers, home theater systems, covert camera installations and fire alarm installation and monitoring at competitive prices.</p>
<div class="abs about-circle" style="left:381px;top:2921px;width:383px;height:383px;background:radial-gradient(circle,#e9eef2 0%,#c9d2da 45%,#2d3238 80%)" role="img" aria-label="Presenter on stage in front of a large screen"></div>
<p class="abs about-text" style="left:150px;top:3372px;width:424px">Call 713-555-0142, Monday–Friday 8am–5pm. Write to P.O. Box 419 Crosby, TX 77064 or email Northgatess@ferntopmail.com. Company license #K52948316. Fire license #TMV-6614027, JLP-8170326.</p>
<div class="abs about-circle" style="left:627px;top:3318px;width:392px;height:392px;background:radial-gradient(circle,#f1f0ee 0%,#dedad6 55%,#a9a3a0 100%)" role="img" aria-label="Desk with laptop, ribbon and stationery seen from above"></div>

<h2 class="abs contact-title">CONTACT US TODAY FOR:</h2>
<div class="abs offer-photo" style="left:232px;background:linear-gradient(135deg,#dfe6ee,#3b7fd0);border:4px solid #2b5c9c" role="img" aria-label="Smartphone with app icons"></div>
<div class="abs offer-label" style="left:340px;background:var(--label-blue)">THE<br>HOTTEST<br><b>TRENDS</b></div>
<div class="abs offer-photo" style="left:552px;background:linear-gradient(135deg,#b5743e,#8c5a2c);border:4px solid #7d2b1e" role="img" aria-label="Yellow sticky note with a light bulb on a cork board"></div>
<div class="abs offer-label" style="left:662px;background:var(--label-red)">BUDGET<br>FRIENDLY<br><b>IDEAS</b></div>
<div class="abs offer-photo" style="left:871px;background:linear-gradient(135deg,#7b5a44,#d9d6d2);border:4px solid #a04d1a" role="img" aria-label="Notebook, paints and brushes on a wooden table"></div>
<div class="abs offer-label" style="left:982px;width:165px;background:var(--label-orange);text-align:left;padding-left:8px">CUSTOMIZED<br><b>PROPOSALS</b></div>

<form>
  <label class="abs field-label" style="left:165px;top:3970px">Email</label>
  <div class="abs field" style="left:165px;top:3996px;width:431px"></div>
  <label class="abs field-label" style="left:165px;top:4038px">Address</label>
  <div class="abs field" style="left:165px;top:4062px;width:868px">1234 Main St</div>
  <label class="abs field-label" style="left:165px;top:4106px">Address 2</label>
  <div class="abs field" style="left:165px;top:4130px;width:868px">Apartment, studio, or floor</div>
  <label class="abs field-label" style="left:165px;top:4173px">City</label>
  <label class="abs field-label" style="left:603px;top:4173px">State</label>
  <label class="abs field-label" style="left:895px;top:4173px">Zip</label>
  <div class="abs field" style="left:165px;top:4197px;width:431px"></div>
  <div class="abs field" style="left:603px;top:4197px;width:285px">Choose...
    <svg class="select-caret" width="9" height="6" viewBox="0 0 9 6"><path d="M1 1 L4.5 5 L8 1" fill="none" stroke="#343a40" stroke-width="1.4"/></svg>
  </div>
  <div class="abs field" style="left:895px;top:4197px;width:138px"></div>
  <div class="abs check-row"><span class="check-box"></span>Check me out</div>
  <div class="abs send-button">Send Message</div>
</form>

<footer class="abs site-footer">
  <p class="abs footer-text">© Northgate Signal Shield LLC · A great place for your security needs · Licensed and insured · 713-555-0142 · Monday–Friday 8am–5pm · Crosby, TX</p>
</footer>

</body>
</html>
```